Corporate Website - KALDRA HOLDINGS, LLC

This Nevada Corporation has several subsidiaries:
T. M. Designs - Interior Design; Commercial, Residential & Hospitality
T. M. Style - Fashion Design & Styling
VERN LOUNGE - Upscale Membership Only Lounge servicing Business Men and women. It is located in Accra, Ghana
VERN SUITES - Full Service Executive Suites for top Businesses. Located in Accra, Ghana.
THE MATERIAL NOOK - Distributor for Building and Interior Design Materials
URL: www.kaldraholdingsllc.example
Website: info@kaldraholdingsllc.example
Phones: 1 702-555-0147 Las Vegas; +233 26 5550193 Ghana

Industry/Entity Type

Fashion

```html
<!DOCTYPE html>
<html lang="en">
<head>
<meta charset="utf-8">
<title>Kaldra Holdings, LLC.</title>
<link href="https://fonts.googleapis.com/css2?family=Figtree:wght@400;500;600;700&display=swap" rel="stylesheet">
<style>
:root{
  --ink:#232425;
  --ink-deep:#1b1c1d;
  --blue:#1a9fe0;
  --paper:#ffffff;
  --mist:#eeeeee;
  --line:#9a9a9a;
  --caption:rgba(35,35,35,.72);
  --muted:#555;
}
*{box-sizing:border-box;margin:0;padding:0}
html,body{width:823px;height:1200px;overflow:hidden}
body{position:relative;background:var(--paper);font-family:"Figtree",Arial,sans-serif;color:var(--ink)}
.abs{position:absolute}
.site-header{left:0;top:0;width:823px;height:44px;background:var(--ink)}
.brand{left:110px;top:14px;color:#fff;font-weight:700;font-size:12.5px;letter-spacing:.1px}
.main-nav{left:395px;top:17px;display:flex;gap:11px;font-size:8.5px;font-weight:500;color:#fff}
.main-nav .active{color:var(--blue)}
.nav-icon{top:16px}
.tile{overflow:hidden}
.photo{width:100%;height:100%}
.caption{position:absolute;left:0;bottom:0;width:100%;height:41px;background:var(--caption);color:#fff;padding:10px 10px 0}
.caption small{display:block;font-size:7.5px;line-height:9px}
.caption strong{display:block;font-weight:500;font-size:10.5px;line-height:13px}
.caption strong::after{content:" ›";font-weight:700}
.play{left:172px;top:125px}
.section-title{width:823px;text-align:center;color:var(--blue);font-weight:400}
.tour-band{position:absolute;left:0;bottom:0;width:100%;height:40px;background:var(--caption);color:#fff;font-size:18px;padding:9px 15px}
.dots{position:absolute;right:16px;top:16px;display:flex;gap:3px}
.dots i{width:6px;height:6px;border-radius:50%;background:#fff}
.dots i.on{background:var(--blue)}
.callback{left:522px;top:612px;width:190px;height:248px;background:var(--mist);padding:28px 19px 0}
.callback p{font-size:7.5px;font-weight:500}
.callback h3{color:var(--blue);font-size:14px;font-weight:500;line-height:15px;margin:6px 0 8px}
.callback label{display:block;font-size:7px;font-weight:600;margin-bottom:3px}
.field{height:19px;width:152px;border:1px solid #999;border-radius:2px;background:var(--mist);margin-bottom:11px}
.btn{background:var(--blue);color:#fff;text-align:center;font-size:7.5px;font-weight:500}
.callback .btn{height:19px;width:152px;line-height:19px;border-radius:2px}
.newsletter{left:0;top:886px;width:823px;height:114px;background:var(--mist)}
.subscribe-input{left:213px;top:950px;width:260px;height:25px;border:1px solid #bbb;background:#fff;font-size:7.5px;color:#777;padding:8px 11px}
.subscribe-btn{left:472px;top:950px;width:137px;height:25px;line-height:25px;font-size:8.5px}
.site-footer{left:0;top:1000px;width:823px;height:163px;background:#262728;color:#fff}
.foot-col h4{color:var(--blue);font-size:9.5px;font-weight:600;margin-bottom:10px}
.foot-col p,.foot-col li{font-size:7.3px;line-height:14.5px}
.foot-col ul{list-style:none}
.foot-col li{line-height:15.5px}
.divider{width:1px;height:115px;background:#444;top:1025px}
.contact-item{display:flex;gap:8px;margin-bottom:12px;font-size:7.3px;line-height:12px}
.dot{width:14px;height:14px;border-radius:50%;flex:none;margin-top:2px}
.legal{left:0;top:1163px;width:823px;height:37px;background:var(--ink-deep)}
.legal p{position:absolute;left:110px;top:14px;color:#fff;font-size:6.8px}
.social{position:absolute;top:10px;width:17px;height:17px;border-radius:50%}
</style>
</head>
<body>
<header class="site-header abs">
  <div class="brand abs">Kaldra Holdings, LLC.</div>
  <nav class="main-nav abs"><span class="active">HOME</span><span>COLLECTION</span><span>ABOUT</span><span>NEWS</span><span>MATERIALS</span><span>CONTACT</span></nav>
  <svg class="nav-icon abs" style="left:678px" width="12" height="11" viewBox="0 0 12 11" fill="none" stroke="#fff" stroke-width="1.2"><path d="M0 1h2l2 6h6l1.5-4.5H3"/><circle cx="5" cy="9.5" r=".8"/><circle cx="9" cy="9.5" r=".8"/></svg>
  <svg class="nav-icon abs" style="left:702px" width="11" height="11" viewBox="0 0 11 11" fill="none" stroke="#fff" stroke-width="1.4"><circle cx="4.5" cy="4.5" r="3.4"/><path d="M7 7l3.5 3.5"/></svg>
</header>

<article class="tile abs" style="left:110px;top:60px;width:191px;height:142px">
  <div class="photo" role="img" aria-label="Quilted pale wall with a black pendant lamp" style="background:linear-gradient(135deg,#d8d3d0,#b9b3b0)"></div>
  <div class="caption"><small>Interior Design</small><strong>Consectetur adipiscing elit, sed do</strong></div>
</article>
<article class="tile abs" style="left:110px;top:218px;width:191px;height:142px">
  <div class="photo" role="img" aria-label="Striped vases on a marble table beside a grey sofa" style="background:linear-gradient(120deg,#5e5e62,#2d2f35 55%,#8a8580)"></div>
  <div class="caption"><small>Hospitality</small><strong>Lorem ipsum dolor sit amet</strong></div>
</article>
<article class="tile abs" style="left:316px;top:60px;width:396px;height:300px">
  <div class="photo" role="img" aria-label="White room with a long table, two chairs and pendant lamps" style="background:linear-gradient(180deg,#c9c9c9,#e6e6e6 40%,#d4d4d4 75%,#b8b8b8)"></div>
  <svg class="play abs" width="52" height="52" viewBox="0 0 52 52"><circle cx="26" cy="26" r="24" fill="none" stroke="#fff" stroke-width="2.5"/><path d="M21 17l14 9-14 9z" fill="#fff"/></svg>
  <div class="caption"><small>Commercial</small><strong>Consectetur adipiscing elit, sed do</strong></div>
</article>

<h2 class="section-title abs" style="top:382px;font-size:17.5px">Featured Collection</h2>

<article class="tile abs" style="left:110px;top:413px;width:139px;height:173px">
  <div class="photo" role="img" aria-label="Close view of quilted dark faux leather" style="background:linear-gradient(135deg,#4a4846,#262524)"></div>
  <div class="caption"><small>Faux Leathers</small><strong>Lorem ipsum dolor</strong></div>
</article>
<article class="tile abs" style="left:265px;top:413px;width:139px;height:173px">
  <div class="photo" role="img" aria-label="Bright commercial interior with wood and green accents" style="background:linear-gradient(160deg,#c9c2b4,#8fa48c 50%,#a07a55)"></div>
  <div class="caption"><small>Commercial</small><strong>Lorem ipsum dolor</strong></div>
</article>
<article class="tile abs" style="left:419px;top:413px;width:139px;height:173px">
  <div class="photo" role="img" aria-label="Lobby with a warm wooden lattice wall and reception desk" style="background:linear-gradient(160deg,#5b3a22,#a8753f 50%,#3c2a1e)"></div>
  <div class="caption"><small>Commercial</small><strong>Lorem ipsum dolor</strong></div>
</article>
<article class="tile abs" style="left:573px;top:413px;width:139px;height:173px">
  <div class="photo" role="img" aria-label="Meeting room with a long pale table and a white pendant lamp" style="background:linear-gradient(170deg,#eeeeec,#cfc6b8 60%,#a89c8a)"></div>
  <div class="caption"><small>Commercial</small><strong>Lorem ipsum dolor</strong></div>
</article>

<article class="tile abs" style="left:110px;top:612px;width:396px;height:248px">
  <div class="photo" role="img" aria-label="Tall atrium with glass windows and a black staircase" style="background:linear-gradient(180deg,#bdbdbb,#d8d8d6 45%,#8a8782)"></div>
  <div class="tour-band">Virtual Tour<div class="dots"><i class="on"></i><i></i><i></i><i></i></div></div>
</article>

<form class="callback abs">
  <p>We would love to talk to you</p>
  <h3>Let us call you for<br>more info</h3>
  <label>Name</label><div class="field"></div>
  <label>Telephone</label><div class="field"></div>
  <label>Email</label><div class="field"></div>
  <div class="btn">Send</div>
</form>

<section class="newsletter abs">
  <h2 class="section-title abs" style="top:22px;font-size:17px">Subscribe to Our Newsletter</h2>
  <p class="abs" style="top:45px;width:823px;text-align:center;font-size:8.5px;color:var(--muted)">Enter your email address below to receive site offers discounts, and promotions</p>
</section>
<div class="subscribe-input abs">Enter your email</div>
<div class="subscribe-btn btn abs">Subscribe</div>

<footer class="site-footer abs">
  <div class="foot-col abs" style="left:148px;top:24px;width:160px">
    <h4>ABOUT US</h4>
    <p>Lorem ipsum dolor sit amet, consectetur adipiscing elit, sed do eiusmod tempor incididunt ut labore et dolore magna aliqua. Ut enim ad minim veniam, quis nostrud exercitation ullamco laboris nisi ut aliquip ex ea. commodo consequat.</p>
  </div>
  <div class="foot-col abs" style="left:389px;top:24px;width:190px">
    <h4>CONTACT DETAILS</h4>
    <div class="contact-item"><span class="dot" style="background:#5bb89a"></span><span>1332 Lorem Ipsum,<br>Accra, Ghana</span></div>
    <div class="contact-item"><span class="dot" style="background:#5c9fce"></span><span>Give us a call<br>(01) 702-555-0147 &nbsp;/ (233) 265 550 193</span></div>
    <div class="contact-item"><span class="dot" style="background:#e8944b"></span><span>Drop us a mail<br>info@kaldraholdingsllc.example</span></div>
  </div>
  <div class="foot-col abs" style="left:630px;top:24px">
    <h4>OUR LINK</h4>
    <ul><li>Home</li><li>Collection</li><li>About</li><li>News</li><li>Materials</li><li>Contact Us</li></ul>
  </div>
</footer>
<div class="divider abs" style="left:334px"></div>
<div class="divider abs" style="left:595px"></div>

<div class="legal abs">
  <p>Copyright © 2015 KALDRA HOLDINGS, LLC. All Rights Reserved.</p>
  <span class="social" style="left:648px;background:#4aa3df" aria-label="Social link"></span>
  <span class="social" style="left:672px;background:#3b5a9a" aria-label="Social link"></span>
  <span class="social" style="left:696px;background:#d9453a" aria-label="Social link"></span>
</div>
</body>
</html>
```